Clean Chic Simple Black & White One sided Biz Card

I need a business card for my company Brightwater Docket Partners. We are a luxury, white glove service for organizing files for attorneys.
I would like something that is stunningly simple and chic/sexy. This is going to be only one sided. We are going to use raised ink or ink embossing for the printing. So the logo will be raised in black. I am currently waiting to hear back from the printer as to whether or not the logo has to be in all black or can be left in its current state of black with grey initials. Please check our website for inspiration. www.brightwaterdocketpartners.example.
Thank you so much for your time.

* Please decide whichever title you think looks best(Chief Executive Officer, CEO, or President)
Updates

I really like the designs that make the logo large and the main focus.  
I also like the use of modern, masculine, simple, chic fonts for the slogan and info.

1) No bold font on slogan or info
2) Shrink info to be smaller maybe to make the logo bigger and more the focus
3) Maybe use grey for all the info and slogan so the focus will be on the logo

Thank you so much for your time!!

Target Market(s)

Luxury driven lawyers and their support staff

Industry/Entity Type

Printer

Requirements
Must have
• One sided card

Modern, sleek, masculine, chic, simple font.

Please add our slogan. Refer to file labeled "old logo" to see how we added our slogan under the old logo.
The slogan is, "Calm Precision for Every Case Record"

Please include the info below:
Marina Thornbury (Chief Executive Officer, CEO, or President)
812 North Delmont Avenue, Suite 1400
Los Angeles, California 90017
P: (213)555-0186 F: (213)555-0142
marinat@brightwaterdocketpartners.example
www.brightwaterdocketpartners.example

Please refer to attached file labeled "inkpressingembossing requirements" for requirements from my printer. Thank you!
Nice to have
• It can be super simple with just the logo and my info. Or it could maybe have some cool feature. Just clean please.

I would prefer the info not be in bold. I think this will help the Logo stand out as the main focus.

I attached files of how the ink pressing and embossing will look.
Should not have
• No crazy shapes and no color other than black with a white background. The logo should be the focus since it will be embossed.

```html
<!DOCTYPE html>
<html lang="en">
<head>
<meta charset="utf-8">
<title>Brightwater Docket Partners — Business Card</title>
<link rel="stylesheet" href="https://fonts.googleapis.com/css2?family=Arimo&family=Tinos:ital,wght@0,700;1,400&display=swap">
<style>
  :root {
    --paper: #ffffff;
    --ink: #000000;
    --mark-grey: #a9b5b5;
    --name-grey: #b3bbbb;
    --info-grey: #d9dddd;
    --slogan-ink: #1a1a1a;
  }
  html, body {
    margin: 0;
    padding: 0;
    overflow: hidden;
    background: var(--paper);
  }
  .card {
    position: relative;
    width: 1200px;
    height: 656px;
    background: var(--paper);
    overflow: hidden;
  }
  .brand {
    position: absolute;
    top: 0;
    left: 0;
    width: 1200px;
    height: 356px;
    text-align: center;
  }
  .brand-mark {
    position: absolute;
    left: 525px;
    top: 30px;
    width: 150px;
    height: 150px;
  }
  .brand-name {
    position: absolute;
    top: 226px;
    left: 0;
    width: 1200px;
    margin: 0;
    font-family: "Tinos", "Times New Roman", serif;
    font-weight: 700;
    font-size: 30px;
    line-height: 36px;
    letter-spacing: 0.24em;
    color: var(--ink);
    text-transform: uppercase;
  }
  .slogan {
    position: absolute;
    top: 268px;
    left: 0;
    width: 1200px;
    margin: 0;
    font-family: "Tinos", "Times New Roman", serif;
    font-style: italic;
    font-size: 32px;
    line-height: 40px;
    color: var(--slogan-ink);
  }
  .info-band {
    position: absolute;
    left: 0;
    top: 356px;
    width: 1200px;
    height: 300px;
    background: var(--ink);
  }
  .info-frame {
    position: absolute;
    left: 0;
    top: 0;
  }
  .person {
    position: absolute;
    left: 53px;
    top: 82px;
    font-family: "Arimo", Arial, sans-serif;
  }
  .person-name {
    margin: 0;
    font-size: 36px;
    line-height: 1;
    color: var(--name-grey);
    text-transform: uppercase;
    letter-spacing: -0.01em;
  }
  .person-title {
    margin: 12px 0 0;
    font-size: 27px;
    color: var(--name-grey);
  }
  .contact {
    position: absolute;
    right: 53px;
    top: 42px;
    margin: 0;
    font-family: "Arimo", Arial, sans-serif;
    font-style: normal;
    font-size: 27px;
    line-height: 40px;
    color: var(--info-grey);
    text-align: right;
  }
</style>
</head>
<body>
  <div class="card">
    <header class="brand">
      <svg class="brand-mark" viewBox="0 0 150 150" aria-hidden="true">
        <circle cx="75" cy="75" r="72" fill="var(--mark-grey)"/>
      </svg>
      <h1 class="brand-name">Brightwater Docket Partners, Inc.</h1>
      <p class="slogan">“Calm Precision for Every Case Record”</p>
    </header>

    <section class="info-band">
      <svg class="info-frame" width="1200" height="300" viewBox="0 0 1200 300" aria-hidden="true">
        <rect x="16" y="15" width="1168" height="268" fill="none" stroke="var(--paper)" stroke-width="5"/>
      </svg>
      <div class="person">
        <p class="person-name">Marina Thornbury</p>
        <p class="person-title">President</p>
      </div>
      <address class="contact">
        812 North Delmont Avenue, Suite 1400<br>
        Los Angeles, California 90017<br>
        P: (213)555-0186 F: (213)555-0142<br>
        marinat@brightwaterdocketpartners.example<br>
        www.brightwaterdocketpartners.example
      </address>
    </section>
  </div>
</body>
</html>
```